7 P's for Healthcare Companies - Textbook Graphic

Can you create a graphic for me for a medical textbook? The goal is to show 7 critical features of a healthcare startup and the audience is physicians with limited business backgrounds.

Please include a picture of young, male emergency physician in the middle of the graphic. Show them evaluating an idea. Can you surround the physician with bold writing for the seven components, and use brief descriptions and simple images or graphics to illustrate the point?

The image should be somewhat formal, but it's OK to be lighthearded.

The seven P's and brief descriptions include the following:
Product: what is their market solution?
(Intellectual) Property: do they have a patent or trademark?
Product Clearance: how will they get KLN approval and TPR clearance?
Payment: how will they make money?
Pilots: have they applied their product in a healthcare setting?
Physician and Patient feedback: Do doctors and patients like their product?
Publication: do they have evidence their product works?

More detail and information is available at this website: https://quvenlo.com/blog/uncategorized/healthcare-framework/

I will need to own this image

```html
<!DOCTYPE html>
<html lang="en">
<head>
<meta charset="utf-8">
<title>7 P's for Healthcare Companies</title>
<link href="https://fonts.googleapis.com/css2?family=Montserrat:wght@500;800;900&display=swap" rel="stylesheet">
<style>
  :root {
    --navy: #1f2b3c;
    --white: #ffffff;
    --cream: #eeebe3;
    --grey: #d9d8d4;
  }
  html, body {
    margin: 0;
    padding: 0;
    width: 1200px;
    height: 1200px;
    overflow: hidden;
    background: var(--white);
  }
  .canvas {
    position: relative;
    width: 1200px;
    height: 1200px;
    background: var(--white);
    font-family: "Montserrat", Arial, sans-serif;
    color: var(--navy);
  }
  .diagram {
    position: absolute;
    inset: 0;
  }
  .physician-art {
    position: absolute;
    left: 456px;
    top: 345px;
    width: 308px;
    height: 363px;
    border-radius: 140px 140px 20px 20px;
    background: linear-gradient(180deg, var(--grey) 0%, var(--cream) 55%, var(--cream) 100%);
  }
  .title {
    position: absolute;
    left: 0;
    width: 1200px;
    top: 654px;
    text-align: center;
    font-weight: 900;
    font-size: 160px;
    line-height: 1;
    letter-spacing: -4px;
    transform: scaleX(0.86);
    color: var(--navy);
    text-shadow: 6px 6px 0 var(--white), -6px -6px 0 var(--white), 6px -6px 0 var(--white), -6px 6px 0 var(--white), 0 8px 0 var(--white), 0 -8px 0 var(--white), 8px 0 0 var(--white), -8px 0 0 var(--white);
  }
  .label {
    position: absolute;
    font-weight: 800;
    font-size: 18.5px;
    line-height: 1.1;
    text-transform: uppercase;
    letter-spacing: 0;
    white-space: nowrap;
  }
  .label .cap {
    font-weight: 500;
    font-size: 62px;
    line-height: 0.72;
    letter-spacing: -5px;
    margin-right: -1px;
  }
  .label .sub {
    display: block;
    text-align: center;
  }
  .label .note {
    position: absolute;
    font-size: 7.5px;
    font-weight: 800;
    left: 36px;
    top: 22px;
  }
  .label--publication { left: 386px; top: 117px; }
  .label--product { left: 717px; top: 117px; }
  .label--property { left: 972px; top: 368px; }
  .label--clearance { left: 857px; top: 912px; }
  .label--payment { left: 559px; top: 1034px; }
  .label--pilots { left: 228px; top: 892px; }
  .label--feedback { left: 118px; top: 331px; }
</style>
</head>
<body>
<div class="canvas">

  <svg class="diagram" width="1200" height="1200" viewBox="0 0 1200 1200">
    <circle class="ring" cx="611" cy="598" r="343" fill="none" stroke="#1f2b3c" stroke-width="19"/>

    <g class="nodes" fill="#1f2b3c">
      <circle cx="461" cy="286" r="93"/>
      <circle cx="761" cy="284" r="93"/>
      <circle cx="949" cy="519" r="93"/>
      <circle cx="882" cy="811" r="93"/>
      <circle cx="612" cy="939" r="93"/>
      <circle cx="342" cy="811" r="93"/>
      <circle cx="276" cy="520" r="93"/>
    </g>

    <g class="icons" fill="none" stroke="#ffffff" stroke-width="2.6" stroke-linecap="round" stroke-linejoin="round">
      <g class="icon-megaphone" transform="translate(461 286)">
        <path d="M-36 6 L-14 -2 L10 -30 L28 16 L-8 24 L-30 24 Q-40 20 -36 6 Z"/>
        <ellipse cx="19" cy="-7" rx="10" ry="24" transform="rotate(-20 19 -7)"/>
        <path d="M-4 24 L6 42 Q10 50 2 50 Q-2 50 -6 44 L-16 26"/>
        <path d="M34 -26 Q44 -10 38 8"/>
        <path d="M42 -36 Q56 -10 46 16"/>
      </g>
      <g class="icon-product" transform="translate(761 284)">
        <path d="M-48 -4 L0 -24 L48 -4 L0 16 Z"/>
        <path d="M-48 -4 L-48 42 L0 62 L48 42 L48 -4"/>
        <path d="M0 16 L0 62"/>
        <circle cx="0" cy="-42" r="13"/>
        <path d="M-6 -28 L-6 -20 L6 -20 L6 -28 M-4 -16 L4 -16"/>
        <path d="M0 -64 L0 -70 M-20 -56 L-25 -62 M20 -56 L25 -62 M-30 -40 L-37 -42 M30 -40 L37 -42"/>
      </g>
      <g class="icon-property" transform="translate(949 519)">
        <path d="M-30 -48 L36 -48 Q46 -48 46 -36 L46 -26 L38 -26 L38 50 Q38 58 30 58 L-34 58 Q-44 58 -44 48 L-44 40 L-30 40 Z"/>
        <path d="M36 -48 Q30 -48 30 -36 L30 -26 L38 -26"/>
        <path d="M-18 -34 L20 -34 M-18 -24 L20 -24 M-18 -14 L8 -14"/>
        <circle cx="8" cy="12" r="12"/>
        <circle cx="8" cy="12" r="5"/>
        <path d="M0 22 L-4 36 L2 33 L6 38 M16 22 L20 36 L14 33 L10 38"/>
      </g>
      <g class="icon-clearance" transform="translate(882 811)">
        <rect x="-34" y="-50" width="68" height="110" rx="6"/>
        <rect x="-12" y="-58" width="24" height="14" rx="3"/>
        <circle cx="-18" cy="-16" r="9"/>
        <path d="M-22 -16 L-19 -12 L-13 -20"/>
        <circle cx="-18" cy="10" r="9"/>
        <path d="M-22 10 L-19 14 L-13 6"/>
        <path d="M-2 -20 L24 -20 M-2 -10 L24 -10 M-2 8 L24 8 M-2 18 L24 18 M-20 36 L24 36"/>
      </g>
      <g class="icon-payment" transform="translate(612 939)">
        <rect x="-50" y="-52" width="100" height="60" rx="2"/>
        <rect x="-42" y="-44" width="84" height="44"/>
        <circle cx="0" cy="-22" r="17"/>
        <path d="M6 -30 Q0 -34 -5 -30 Q-8 -25 0 -22 Q8 -19 5 -14 Q0 -10 -6 -14 M0 -36 L0 -8"/>
        <path d="M-58 30 Q-40 18 -20 22 L8 26 Q14 30 8 34 L-18 34"/>
        <path d="M8 30 L44 16 Q54 14 50 24 L14 48 L-48 48"/>
      </g>
      <g class="icon-pilots" transform="translate(342 811)">
        <circle cx="-16" cy="-48" r="3.5" fill="#ffffff"/>
        <circle cx="22" cy="-48" r="3.5" fill="#ffffff"/>
        <path d="M-26 -48 L-20 -10 Q-14 14 2 14 Q18 14 24 -10 L30 -48"/>
        <path d="M2 14 L2 40 Q2 62 -20 62 Q-44 62 -42 40 Q-40 30 -28 18"/>
        <circle cx="-38" cy="4" r="12"/>
        <circle cx="-38" cy="4" r="4"/>
      </g>
      <g class="icon-feedback" transform="translate(276 520)">
        <path d="M-60 -44 Q-60 -52 -52 -52 L14 -52 Q22 -52 22 -44 L22 0 Q22 8 14 8 L-38 8 L-56 30 L-56 8 Q-60 8 -60 0 Z"/>
        <path d="M30 -22 L52 -22 Q60 -22 60 -14 L60 30 Q60 38 52 38 L46 38 L46 56 L30 40 L-8 40 Q-16 40 -16 32 L-16 22"/>
        <path d="M-20 -10 L-34 -26 Q-40 -36 -30 -40 Q-24 -42 -20 -34 Q-16 -42 -10 -40 Q0 -36 -6 -26 Z" fill="#ffffff"/>
      </g>
    </g>
  </svg>

  <div class="physician-art" role="img" aria-label="Illustration of a young male emergency physician in a white coat and tie, evaluating an idea"></div>

  <div class="title">7P’S</div>

  <div class="label label--publication"><span class="cap">P</span>ublication</div>
  <div class="label label--product"><span class="cap">P</span>roduct</div>
  <div class="label label--property"><span class="note">(Intellectual)</span><span class="cap">P</span>roperty</div>
  <div class="label label--clearance"><span class="cap">P</span>roduct<span class="sub">Clearance</span></div>
  <div class="label label--payment"><span class="cap">P</span>ayment</div>
  <div class="label label--pilots"><span class="cap">P</span>ilots</div>
  <div class="label label--feedback"><span class="cap">P</span>hysician<span class="sub">and patient</span><span class="sub">feedback</span></div>

</div>
</body>
</html>
```